Real Estate Agent Service Brochure

I need a trifold brochure to showcase my real estate services. I am a veteran Real Estate Broker specializing in marketing properties for sale and for top dollar. I would like to see designs that use colors from my logo (attached) and I would like to showcase some before and after photos of staging jobs I have done to homes to get them ready for the market. This brochure is specific to home sellers. You are happy to go check out my website for inspiration www.lomavertpa.com but keep the copy as I have written it. The the final design should communicate experienced professional who uses current technologies and strategies to market properties for the highest value.

Target Market(s)

Homeowners wanting to sell their homes

Industry/Entity Type

Real Estate Agent

Font styles to use
Serif

Requirements
Must have
• My, logo, personal photo, title and contact information as listed:
• Marta Venholt
• Owner Broker
• Stager Re-Designer
• 860-912-7048
• BRAVE Realty LLC
• LOMAVERTPA.com
• Marta@LOMAVERTPA.com
• The colors used should be those in my logo.
• Brochure should be able to fit in standard envelope for mailing.
Nice to have
• I think I would like my personal photo and contact information on the front panel.
Should not have
• Bright colors.

```html
<!DOCTYPE html>
<html lang="en">
<head>
<meta charset="utf-8">
<title>BRAVE Realty LLC – Seller Brochure</title>
<link href="https://fonts.googleapis.com/css2?family=Open+Sans:ital,wght@0,400;0,600;0,700;1,600&family=Great+Vibes&display=swap" rel="stylesheet">
<style>
:root{
  --navy:#141850;
  --navy-deep:#0c0f3c;
  --white:#ffffff;
  --paper:#f4f4f6;
  --ink:#1b1d3a;
  --bg:#d9d6d1;
  --photo-warm-1:#b79a7a;
  --photo-warm-2:#5b4636;
  --photo-cool-1:#dfe2e6;
  --photo-cool-2:#8f9199;
}
*{box-sizing:border-box;margin:0;padding:0}
html,body{width:1200px;height:1200px;overflow:hidden;background:var(--bg)}
body{position:relative;font-family:"Open Sans",sans-serif;color:var(--ink)}
.spread{position:absolute;left:240px;width:720px;box-shadow:0 4px 14px rgba(0,0,0,.25);overflow:hidden}
.spread--outside{top:22px;height:563px;background:var(--navy)}
.spread--inside{top:606px;height:572px;background:var(--paper)}

/* outside: gallery panel */
.ba-card{position:absolute;left:23px;width:201px;border:2px solid var(--white);background:var(--white)}
.ba-card--one{top:22px;height:255px}
.ba-card--two{top:287px;height:252px}
.ba-photo{width:100%;height:50%;display:block}
.ba-photo--before{background:linear-gradient(160deg,var(--photo-warm-1),var(--photo-warm-2))}
.ba-photo--after{background:linear-gradient(160deg,var(--photo-cool-1),var(--photo-cool-2))}
.ba-tag{position:absolute;left:50%;transform:translateX(-50%);font-size:7.5px;font-weight:700;letter-spacing:.3px;text-align:center}
.ba-tag--before{top:calc(50% - 18px);width:70px;height:18px;background:var(--navy);color:var(--white);line-height:18px;clip-path:polygon(18% 0,82% 0,100% 100%,0 100%)}
.ba-tag--after{top:50%;width:70px;height:22px;background:var(--white);color:var(--navy);line-height:12px;clip-path:polygon(0 0,100% 0,50% 100%)}

/* outside: cover area */
.cover{position:absolute;left:247px;top:0;width:473px;height:563px}
.cover-art{position:absolute;left:0;top:0}
.fold{position:absolute;top:0;bottom:0;width:1px;background:rgba(0,0,0,.18)}
.intro-title{position:absolute;left:0;width:241px;top:336px;text-align:center;color:var(--white);font-weight:600;font-size:11.5px}
.intro-text{position:absolute;left:22px;width:197px;top:368px;text-align:center;color:var(--white);font-size:9.3px;line-height:18px}
.intro-text em{font-weight:700}
.brand{position:absolute;left:241px;width:232px;top:95px;text-align:center;color:var(--navy);font-weight:700;line-height:1}
.brand__name{font-size:34px;letter-spacing:1px}
.brand__sub{font-size:9px;letter-spacing:4px;margin-top:4px}
.portrait{position:absolute;left:358px;top:212px;width:115px;height:243px;background:linear-gradient(180deg,#b8b3ad,#3a3b46 60%,#1a1b29)}
.agent{position:absolute;left:262px;top:376px;color:var(--white)}
.agent__name{font-family:"Great Vibes",cursive;font-size:15px}
.agent__role{font-size:7.5px;line-height:11px;font-style:italic;padding-left:2px}
.agent__role span::before{content:"\25C6";font-size:5px;margin-right:4px;vertical-align:middle}
.contact{position:absolute;left:303px;top:468px;color:var(--white);font-weight:600}
.contact__phone{font-size:14px;display:flex;align-items:center;gap:6px}
.contact__mail{font-size:9px;display:flex;align-items:center;gap:6px;margin-top:6px}
.icon{display:block;flex:none}

/* inside */
.panel-left{position:absolute;left:0;top:0;width:242px;height:100%;background:var(--navy);color:var(--white);padding:22px 18px 0 18px}
.panel-left p{font-size:7.5px;line-height:9.6px;text-align:justify;margin-bottom:9px}
.panel-left .lead{font-weight:700}
.toggle{position:absolute;left:72px;top:248px;display:flex;border:1.5px solid var(--white);border-radius:10px;overflow:hidden;font-size:7.5px;font-weight:700}
.toggle span{padding:2px 10px}
.toggle .is-before{background:var(--navy);color:var(--white)}
.toggle .is-after{background:var(--white);color:var(--navy)}
.grid{position:absolute;left:16px;top:268px;width:213px;display:grid;grid-template-columns:1fr 1fr;gap:3px}
.grid div{height:66px}
.grid .b{background:linear-gradient(150deg,#8a6a4d,#3b2a20)}
.grid .a{background:linear-gradient(150deg,#d8b884,#7b5a3a)}

.panel-mid{position:absolute;left:242px;top:0;width:242px;height:100%;background:var(--paper)}
.quote-head{position:absolute;left:14px;width:214px;top:28px;text-align:center;font-weight:700;font-size:10px;line-height:14px;color:var(--navy)}
.quote-mark{position:absolute;font-family:Georgia,serif;font-size:26px;font-weight:700;color:var(--navy);line-height:1}
.review{position:absolute;border:1.5px solid var(--ink);border-radius:5px;background:var(--white);padding:3px 5px 2px;font-size:7.5px;line-height:9.3px;text-align:justify}
.review__by{display:flex;justify-content:space-between;font-weight:700;font-style:italic;margin-top:1px}
.review__by b{font-style:normal;letter-spacing:1px;font-size:7px}
.panel-mid .review{left:9px;width:226px}

.panel-right{position:absolute;left:484px;top:0;width:236px;height:100%;background:var(--paper)}
.panel-right .review{left:8px;width:220px}
.brand--small{left:auto;right:14px;width:auto;top:14px;text-align:center}
.brand--small .brand__name{font-size:17px;letter-spacing:.5px}
.brand--small .brand__sub{font-size:5px;letter-spacing:2px;margin-top:2px}
.about{position:absolute;left:0;top:322px;width:236px;height:250px;background:var(--navy);color:var(--white);padding:14px 10px 0 14px}
.about p{font-size:7.1px;line-height:9px;text-align:justify;margin-bottom:9px}
.about .strong{font-weight:700}
</style>
</head>
<body>

<section class="spread spread--outside" aria-label="Brochure outside">
  <div class="ba-card ba-card--one">
    <div class="ba-photo ba-photo--before" role="img" aria-label="Before staging: empty open-plan living room and staircase"></div>
    <div class="ba-photo ba-photo--after" role="img" aria-label="After staging: furnished dining area and living room"></div>
    <div class="ba-tag ba-tag--before">BEFORE</div>
    <div class="ba-tag ba-tag--after">AFTER</div>
  </div>
  <div class="ba-card ba-card--two">
    <div class="ba-photo ba-photo--before" role="img" aria-label="Before staging: empty room with stone fireplace"></div>
    <div class="ba-photo ba-photo--after" role="img" aria-label="After staging: furnished living room with fireplace"></div>
    <div class="ba-tag ba-tag--before">BEFORE</div>
    <div class="ba-tag ba-tag--after">AFTER</div>
  </div>

  <div class="cover">
    <svg class="cover-art" width="473" height="563" viewBox="0 0 473 563">
      <defs>
        <linearGradient id="roomTone" x1="0" y1="0" x2="1" y2="1">
          <stop offset="0" stop-color="#eef0f3"/>
          <stop offset=".55" stop-color="#b9b4ad"/>
          <stop offset="1" stop-color="#6e6760"/>
        </linearGradient>
      </defs>
      <rect width="473" height="330" fill="url(#roomTone)" role="img" aria-label="Bright staged dining room and kitchen interior"/>
      <polygon points="241,0 473,0 473,118 380,176 241,112" fill="#ffffff"/>
      <path d="M0,216 C90,258 170,304 241,318 L473,318 L473,563 L0,563 Z" fill="var(--navy)"/>
      <path d="M241,412 Q360,452 473,458" stroke="#ffffff" stroke-width="2.5" fill="none"/>
    </svg>
    <div class="fold" style="left:241px"></div>

    <div class="brand">
      <div class="brand__name">BRAVE</div>
      <div class="brand__sub">REALTY LLC</div>
    </div>

    <div class="portrait" role="img" aria-label="Portrait of broker Marta Venholt in a dark blazer"></div>

    <h2 class="intro-title">Proven Market Knowledge</h2>
    <p class="intro-text">That’s what you can expect when you work with seasoned specialist <em>Marta Venholt</em> for all your Real Estate needs. The sale of a home is too important an undertaking to entrust to just anyone. Select a dedicated, service-oriented and results-driven broker who understands the intricacies of the Real Estate process...select <em>Marta Venholt</em>.</p>

    <div class="agent">
      <div class="agent__name">Marta Venholt</div>
      <div class="agent__role"><span>Broker Owner</span><br><span>Stager Re-Designer</span></div>
    </div>

    <div class="contact">
      <div class="contact__phone">
        <svg class="icon" width="11" height="11" viewBox="0 0 24 24"><path fill="#fff" d="M6.6 10.8c1.4 2.8 3.8 5.1 6.6 6.6l2.2-2.2c.3-.3.7-.4 1-.2 1.1.4 2.3.6 3.6.6.6 0 1 .4 1 1V20c0 .6-.4 1-1 1C10.6 21 3 13.4 3 4c0-.6.4-1 1-1h3.5c.6 0 1 .4 1 1 0 1.3.2 2.5.6 3.6.1.3 0 .7-.2 1z"/></svg>
        <span>860-912-7048</span>
      </div>
      <div class="contact__mail">
        <svg class="icon" width="10" height="8" viewBox="0 0 20 14"><rect x="1" y="1" width="18" height="12" fill="none" stroke="#fff" stroke-width="2"/><path d="M1 1l9 7 9-7" fill="none" stroke="#fff" stroke-width="2"/></svg>
        <span>Marta@LOMAVERTPA.com</span>
      </div>
    </div>
  </div>
</section>

<section class="spread spread--inside" aria-label="Brochure inside">
  <div class="panel-left">
    <p>Selling Real Estate has changed drastically in the last few years. Today’s real estate processes are multi-faceted undertakings that encompass significant emotional and financial components. Having the right marketing partner is so important; one who works to protect your best interests while capably navigating you through the many complexities of the real estate transaction is vital.</p>
    <p>Marta Venholt Real Estate Marketing Specialist truly understands not only the legal process needed but also recognizes buyer trends and knows how to “showcase” a property to sell targeted to the proper consumer demographic.</p>
    <p class="lead">A home is one of your most valuable assets. If you are thinking about selling a property, it is crucial that you hire someone with an extraordinary history of happy sellers.</p>
    <div class="toggle"><span class="is-before">BEFORE</span><span class="is-after">AFTER</span></div>
    <div class="grid">
      <div class="b" role="img" aria-label="Before: cluttered basement room"></div>
      <div class="a" role="img" aria-label="After: staged basement with exercise area"></div>
      <div class="b" role="img" aria-label="Before: bedroom with mixed furniture"></div>
      <div class="a" role="img" aria-label="After: staged bedroom"></div>
      <div class="b" role="img" aria-label="Before: dark bedroom"></div>
      <div class="a" role="img" aria-label="After: bright staged bedroom"></div>
      <div class="b" role="img" aria-label="Before: kitchen and dining area"></div>
      <div class="a" role="img" aria-label="After: staged dining area"></div>
    </div>
  </div>

  <div class="panel-mid">
    <span class="quote-mark" style="left:14px;top:22px">“</span>
    <h3 class="quote-head">This is what Marta’s clients say<br>about their experiences:</h3>
    <span class="quote-mark" style="right:16px;top:34px">”</span>

    <article class="review" style="top:73px;height:84px">In the Real Estate Business there are many, but none like Marta. She brings a level of professionalism far above other Brokers. She will have no trouble selling your house. What is different is her honesty, sincerity, and unquestionable ethics. She will make sure that you are satisfied with every aspect of your transaction.
      <div class="review__by">- Walter H.<b>★★★★★</b></div></article>
    <article class="review" style="top:165px;height:76px">Marta and the team at Brave are knowledgeable and professional. I have been involved in three separate real estate transactions with Marta as my broker. I am always pleased and impressed by her negotiating skills, her market knowledge and her ability to manage the process.
      <div class="review__by">- Diane L.<b>★★★★★</b></div></article>
    <article class="review" style="top:248px;height:96px">Am so glad that we found Marta to help us in staging a property that we had just finished renovating. She listened to our ideas of what we envisioned in the spaces based on the style of the house and put it all together and on time for the first open house that got rave reviews! Her combined background in real estate and interior design made her a perfect partner for our job.
      <div class="review__by">- Colleen T.<b>★★★★★</b></div></article>
    <article class="review" style="top:352px;height:53px">The marketing and staging of our house was on point. I don't think the sale of our home would have been as successful without it.
      <div class="review__by">- Rob &amp; Tessa W.<b>★★★★★</b></div></article>
    <article class="review" style="top:412px;height:120px">I have had several real estate dealings with Marta each one was handled professionally and with my best interest in mind. Her marketing skills are top notch she made sure my properties where ready for market and showcased them in the best way by staging them and having professional photography done. She helped me get through home inspections issues keeping the sales in tact. I keep using her services and recommend her to family and friends she really knows her stuff!
      <div class="review__by">- Marisa K.<b>★★★★★</b></div></article>
  </div>

  <div class="panel-right">
    <div class="brand brand--small">
      <div class="brand__name">BRAVE</div>
      <div class="brand__sub">REALTY LLC</div>
    </div>
    <article class="review" style="top:64px;height:117px">Marta worked with our builder to help us design new floor plans, she was responsible for all the selections/finishes and then completely staged and decorated the homes using some furniture from old models and also shopping for new furniture. The model homes came out beautiful! The feedback was amazing and all the homes sold quickly! She was responsive with updates and reports. We will be using her services again for our next project!
      <div class="review__by">- Gregory S.<b>★★★★★</b></div></article>
    <article class="review" style="top:189px;height:123px">Marta directed us right from the beginning by preparing a market evaluation using current data, helping us to establish a proper list price; she prepared our property for the market by staging it and then marketed it with great photography and video tours. Because of her pre-marketing preparations we received several offers on our house! Keeping our interests first, Marta negotiated the best deal for us; we were truly blown away by her knowledge, work ethic and professionalism.
      <div class="review__by">- Sam &amp; Lina R.<b>★★★★★</b></div></article>
    <div class="about">
      <p>Marta devotes her efforts to selling real estate, by keeping up with the evolving market, researching buyer trends and preparing homes before they enter the market by staging them to connect with the target buyer. <span class="strong">Marta knows all sales are not alike. Therefore, taking a cookie cutter approach is not acceptable, she recognizes that each property is unique and requires a personalized marketing plan and strategy.</span></p>
      <p class="strong">A veteran in the real estate industry with nearly 30 years expertise and consistent membership in the Multi-Million-Dollar Club combined with her CHS Home Stager and Re-Designer credentials assures that her clients get the advantage of vast knowledge, seasoned experience and proven results, all geared to creating beautiful spaces, which form a connection with the right buyer producing the highest and best offer.</p>
    </div>
  </div>
</section>

</body>
</html>
```